Online counselling service - business cards

We need a business card (front and back) design for a new online counselling and psychotherapy service for people all over the world. We offer voice- and video-chat for clients, as well as instant messaging.
The final design should communicate a fusion of calm, strength and support.

Industry/Entity Type

Business

Requirements
Must have
• The design must contain the following information:
Company name - Quiet Harbour Path
E-mail address - admin@quietharbourpath-example.com
Website address - www.quietharbourpath-example.com

The design must also include the logo (with or without words), as attached below.
Nice to have
• We are open to QR codes being used.
A minimalist approach to design is preferred for the front of the card, with the eye drawn to the name of the company.
Sans-serif fonts only, please.
It would be great to have a space for therapists to put their name (but no other contact details) on the back of the card.
After seeing different designs, I like the feel of rounded corner business cards.
If you want to have a bash at redesigning the logo you are very welcome to do so!
Should not have
• The design should avoid using sharp angles and serif-fonts.

```html
<!DOCTYPE html>
<html lang="en">
<head>
<meta charset="utf-8">
<title>Quiet Harbour Path – Business Cards</title>
<link rel="stylesheet" href="https://fonts.googleapis.com/css2?family=Open+Sans:wght@400;600;700&display=swap">
<style>
  :root {
    --page-bg: #e9e9ee;
    --card-white: #ffffff;
    --band-deep: #1620b8;
    --band-mid: #2f3fe6;
    --band-light: #8f9cff;
    --ink: #111111;
    --accent-blue: #1a2bd6;
    --card-shadow: rgba(40, 40, 70, 0.18);
  }
  * { box-sizing: border-box; margin: 0; padding: 0; }
  html, body {
    width: 1200px;
    height: 900px;
    overflow: hidden;
    background: var(--page-bg);
    font-family: "Open Sans", Arial, sans-serif;
  }
  .canvas {
    position: relative;
    width: 1200px;
    height: 900px;
  }
  .card {
    position: absolute;
    left: 250px;
    width: 700px;
    height: 400px;
    background: var(--card-white);
    border-radius: 28px;
    overflow: hidden;
    box-shadow: 0 10px 28px var(--card-shadow);
  }
  .card--back { top: 40px; }
  .card--front { top: 470px; }

  .band {
    position: absolute;
    top: 0;
    width: 58px;
    height: 100%;
    background: linear-gradient(90deg,
      var(--band-deep) 0%,
      var(--band-mid) 30%,
      var(--band-light) 52%,
      var(--band-mid) 72%,
      var(--band-deep) 100%);
  }
  .band--left { left: 0; }
  .band--right { right: 0; }

  .brand {
    display: flex;
    align-items: center;
    gap: 14px;
    color: var(--ink);
    font-weight: 600;
    white-space: nowrap;
  }
  .brand__dot {
    width: 22px;
    height: 22px;
    border-radius: 50%;
    background: var(--accent-blue);
    flex: none;
  }
  .card--back .brand {
    position: absolute;
    inset: 0;
    justify-content: center;
    font-size: 38px;
  }
  .card--front .brand {
    position: absolute;
    left: 92px;
    top: 76px;
    font-size: 24px;
  }

  .contact {
    position: absolute;
    left: 248px;
    top: 178px;
    width: 372px;
    color: var(--ink);
    white-space: nowrap;
  }
  .contact__name {
    font-size: 40px;
    font-weight: 700;
    letter-spacing: -1px;
    line-height: 1.1;
  }
  .contact__role {
    color: var(--accent-blue);
    font-size: 28px;
    font-weight: 400;
    letter-spacing: 0;
    margin-left: 8px;
  }
  .contact__line {
    font-size: 18px;
    line-height: 1.6;
  }
  .contact__name + .contact__line { margin-top: 10px; }
  .contact__label { font-weight: 700; margin-right: 6px; }
</style>
</head>
<body>
<main class="canvas">
  <section class="card card--back" aria-label="Card back">
    <div class="band band--left"></div>
    <div class="band band--right"></div>
    <div class="brand">
      <span class="brand__dot"></span>
      <span class="brand__name">Quiet Harbour Path</span>
    </div>
  </section>

  <section class="card card--front" aria-label="Card front">
    <div class="band band--left"></div>
    <div class="band band--right"></div>
    <div class="brand">
      <span class="brand__dot"></span>
      <span class="brand__name">Quiet Harbour Path</span>
    </div>
    <div class="contact">
      <p class="contact__name">JOHN DOE<span class="contact__role">manager</span></p>
      <p class="contact__line"><span class="contact__label">e:</span>admin@quietharbourpath-example.com</p>
      <p class="contact__line"><span class="contact__label">w:</span>www.quietharbourpath-example.com</p>
    </div>
  </section>
</main>
</body>
</html>
```